Option Sheet

We need a one page option sheet with a left to right reading of the five options. It should be a one sheet, multiple colors and definitive separations between options This is used in a sales consultation. Backround or colors not in option need to have the follow RGB value (5 red, 20 green, 63 blue)

We added a smaller text file, please change that point

Target Market(s)

Divorce

Industry/Entity Type

Legal

Requirements
Must have
• 1) All five options left to right
• 2)language included in sheet

```html
<!DOCTYPE html>
<html lang="en">
<head>
<meta charset="utf-8">
<title>5 Options Divorce – Option Sheet</title>
<link rel="stylesheet" href="https://fonts.googleapis.com/css2?family=Libre+Baskerville:wght@400;700&family=Open+Sans:wght@400;600&display=swap">
<style>
  :root{
    --navy:#1a1c30;
    --blue-light:#44708f;
    --blue-dark:#2b5577;
    --grey:#e2e2e4;
    --ink:#1a1c30;
    --paper-bg:#d8d5cf;
    --white:#ffffff;
  }
  *{box-sizing:border-box;margin:0;padding:0}
  html,body{width:1200px;height:1200px;overflow:hidden}
  body{background:var(--paper-bg);font-family:"Open Sans",Arial,sans-serif;position:relative}
  .sheet{position:absolute;left:190px;top:20px;width:820px;height:1160px;background:var(--grey);overflow:hidden;box-shadow:0 4px 18px rgba(0,0,0,.18)}
  .sheet-bg{position:absolute;inset:0}

  .title{position:absolute;left:36px;top:70px;color:var(--white);font-family:"Libre Baskerville",Georgia,serif}
  .title-number{position:absolute;left:0;top:0;font-size:200px;line-height:1;font-weight:700}
  .title-words{position:absolute;left:126px;top:34px;font-size:56px;line-height:1.04;font-weight:700;white-space:nowrap}
  .title-rule{position:absolute;left:126px;top:172px;width:250px;height:3px;background:var(--white)}

  .option{position:absolute}
  .option--dark-text{color:var(--ink)}
  .option--light-text{color:var(--white)}
  .option-label{font-family:"Libre Baskerville",Georgia,serif;font-size:20px;text-align:center;margin-bottom:4px}
  .option-name{display:table;min-width:78%;font-family:"Libre Baskerville",Georgia,serif;font-size:29px;font-weight:400;text-align:center;border:1.5px solid currentColor;padding:4px 14px;margin:0 auto 16px;white-space:nowrap}
  .option-cols{display:grid;grid-template-columns:1fr 1px 1.3fr;gap:14px;align-items:center}
  .option-divider{background:currentColor;opacity:.85;align-self:stretch}
  .col-heading{font-size:16px;margin-bottom:7px}
  ul.bullets{list-style:none}
  ul.bullets li{position:relative;padding-left:19px;font-size:14px;line-height:1.24;margin-bottom:8px}
  ul.bullets li::before{content:"";position:absolute;left:2px;top:5px;width:8px;height:8px;border:1.5px solid currentColor;border-radius:50%}

  .opt1{left:448px;top:26px;width:356px}
  .opt2{left:448px;top:350px;width:356px}
  .opt3{left:24px;top:356px;width:394px}
  .opt4{left:24px;top:776px;width:426px}
  .opt4 .option-name{font-size:27px}
  .opt4-extra{position:absolute;left:40px;top:1066px;width:600px;color:var(--ink)}
  .opt5{left:486px;top:738px;width:320px}
  .opt5 .adv-grid{display:grid;grid-template-columns:1fr 1fr;gap:0 12px}
  .opt5 .col-heading{text-align:center}
</style>
</head>
<body>
<main class="sheet">
  <svg class="sheet-bg" width="820" height="1160" viewBox="0 0 820 1160" aria-hidden="true">
    <defs>
      <linearGradient id="blueFade" x1="0" y1="0" x2="0" y2="1">
        <stop offset="0" stop-color="var(--blue-dark)"/>
        <stop offset="1" stop-color="var(--blue-light)"/>
      </linearGradient>
    </defs>
    <rect width="820" height="1160" fill="var(--grey)"/>
    <polygon points="0,0 430,0 430,110 466,140 430,170 430,330 0,330" fill="var(--navy)"/>
    <polygon points="0,330 430,330 430,760 300,760 270,790 240,760 0,760" fill="url(#blueFade)"/>
    <polygon points="430,330 500,330 540,370 580,330 820,330 820,720 430,720 430,560 400,530 430,500" fill="var(--navy)"/>
    <polygon points="470,720 820,720 820,1040 470,1040 470,800 440,770 470,740" fill="var(--blue-dark)"/>
  </svg>

  <header class="title">
    <span class="title-number">5</span>
    <h1 class="title-words">Options<br>Divorce</h1>
    <span class="title-rule"></span>
  </header>

  <section class="option opt1 option--dark-text">
    <p class="option-label">Option #1</p>
    <h2 class="option-name">Do Nothing</h2>
    <div class="option-cols">
      <div><p class="col-heading">Advantages:</p>
        <ul class="bullets"><li>Stay married</li><li>No life Changes</li></ul></div>
      <span class="option-divider"></span>
      <div><p class="col-heading">Disadvantages:</p>
        <ul class="bullets"><li>Remain unhappy, depressed, anxious</li><li>Money and assets may disappear</li><li>What is going to change?</li></ul></div>
    </div>
  </section>

  <section class="option opt2 option--light-text">
    <p class="option-label">Option #2</p>
    <h2 class="option-name">Go to Counseling</h2>
    <div class="option-cols">
      <div><p class="col-heading">Advantages:</p>
        <ul class="bullets"><li>Reconcile marriage</li><li>Help make a better life</li></ul></div>
      <span class="option-divider"></span>
      <div><p class="col-heading">Disadvantages:</p>
        <ul class="bullets"><li>Past issues are highlighted and may drudge up old wounds</li><li>It may just clarify the reasons you need to separate and/or divorce</li><li>Both parties must be invested and willing to participate</li></ul></div>
    </div>
  </section>

  <section class="option opt3 option--light-text">
    <p class="option-label">Option #3</p>
    <h2 class="option-name">Do it Yourself</h2>
    <div class="option-cols">
      <div><p class="col-heading">Advantages:</p>
        <ul class="bullets"><li>No attorney fees</li><li>You are your own attorney</li></ul></div>
      <span class="option-divider"></span>
      <div><p class="col-heading">Disadvantages:</p>
        <ul class="bullets"><li>People often find that what is “fair,” may in fact, not be truly fair</li><li>Often times, people do not know the risks</li><li>Complicated legal system within intrigue rules</li><li>Unsure how to complete the paperwork and meet the deadlines</li></ul></div>
    </div>
  </section>

  <section class="option opt4 option--dark-text">
    <p class="option-label">Option #4</p>
    <h2 class="option-name">Limited Representation</h2>
    <div class="option-cols">
      <div><p class="col-heading">Advantages:</p>
        <ul class="bullets"><li>Balance between going alone and our limited involvement in the case</li></ul></div>
      <span class="option-divider"></span>
      <div><p class="col-heading">Disadvantages:</p>
        <ul class="bullets"><li>Our terms may not benefit from our legal knowledge</li><li>Your spouse or other parties may cause your legal fees to increase significantly without action on your part</li></ul></div>
    </div>
  </section>
  <ul class="bullets opt4-extra"><li>The legal consequences of your legal documents will not be explained to you so that you can formulate a plan for handling the rest of your case.</li></ul>

  <section class="option opt5 option--light-text">
    <p class="option-label">Option #5</p>
    <h2 class="option-name">Hire Us</h2>
    <p class="col-heading">Advantages:</p>
    <ul class="bullets adv-grid">
      <li>Gain the full benefits of our experience</li><li>Often saves you or makes you money in the long run</li>
      <li>Have a team of Family Law focus attorneys</li><li>Save you time, energy and stress</li>
    </ul>
    <p class="col-heading">Disadvantages:</p>
    <ul class="bullets"><li>Initial cost</li></ul>
  </section>
</main>
</body>
</html>
```